Company or website name
- Jardin Lumineux
- Slogan or Tagline
- No Taglines, but each description listed here needs to be on the front label of each of these wines.
- Describe your company and organization and target audience
- Consumers buying wine aged 30+, restaurants. Of wine buyers, 55% are female shopping at major grocery chains.
- The design should have the following
- The style should marry traditional sophistication with a touch of contemporary fun. It should tell knowledgeable wine buyers that it is a serious, quality product, but have enough light to attract the novice wine buyers and impulse buyers. Must have: 1) Jardin Lumineux (brand name) 2) Method Traditionelle 3) Appellation Cremant de Limoux Controlee 4) Product of France -Brut -Brut RoseFountaine de la Vie means "Bright Garden" in French We would like this idea implemented into the design of the label. As a sparkling wine, bubbles are what spring from this fountain.
- This design should not have this in the entries
- No use of Gold or Gold Foil (scratches too easily). Also, black labels tend to scuff and don't travel well (plus they don't stand out on the shelves as much). Not too frilly – this is a quality product. We do not want to turn off serious wine buyers because they don’t take the label seriously.

```html
<!DOCTYPE html>
<html lang="en">
<head>
<meta charset="utf-8">
<title>Jardin Lumineux – Crémant de Limoux Labels</title>
<link rel="stylesheet" href="https://fonts.googleapis.com/css2?family=Cormorant+Garamond:wght@500;600&display=swap">
<style>
  :root {
    --ink-blue: #2b3596;
    --label-cream: #eee39b;
    --paper: #ffffff;
    --glass-green: #1f9a40;
    --glass-green-light: #4cb868;
    --glass-rose: #eea264;
    --glass-rose-light: #f7c79a;
    --foil-light: #e4e6e6;
    --foil-dark: #9b9f9f;
  }
  * { box-sizing: border-box; margin: 0; padding: 0; }
  html, body { width: 1200px; height: 960px; overflow: hidden; background: var(--paper); }
  .canvas { position: relative; width: 1200px; height: 960px; overflow: hidden; background: var(--paper);
    font-family: "Cormorant Garamond", "Times New Roman", serif; color: var(--ink-blue); }
  .bottles { position: absolute; left: 0; top: 0; }

  .front-label { position: absolute; font-size: 10px; }
  .front-label .label-shape { position: absolute; inset: 0; width: 100%; height: 100%; }
  .front-label .label-text { position: absolute; inset: 0; display: flex; flex-direction: column;
    align-items: center; justify-content: center; text-align: center; padding-top: 0.6em; }
  .method { font-size: 1.5em; line-height: 1.05; letter-spacing: 0.04em; font-weight: 500; }
  .brand-name { font-size: 5.2em; line-height: 0.95; font-weight: 600; margin: 0.12em 0 0.18em; }
  .appellation-title { font-size: 2.4em; line-height: 1; font-weight: 500; letter-spacing: 0.02em; }
  .appellation-full { font-size: 1.05em; letter-spacing: 0.04em; font-weight: 500; margin-top: 0.2em; }
  .origin { font-size: 1.05em; letter-spacing: 0.05em; font-weight: 500; margin-top: 1.4em; }

  .label-large { left: 630px; top: 98px; width: 537px; height: 325px; font-size: 10px; }
  .label-on-brut { left: 68px; top: 660px; width: 255px; height: 156px; font-size: 4.75px; }
  .label-on-rose { left: 408px; top: 660px; width: 264px; height: 152px; font-size: 4.75px; }

  .style-tag { position: absolute; display: flex; align-items: center; justify-content: center; }
  .style-tag svg { position: absolute; inset: 0; width: 100%; height: 100%; }
  .style-tag span { position: relative; font-weight: 500; letter-spacing: 0.22em; padding-left: 0.22em; }
  .tag-large-rose { left: 720px; top: 518px; width: 252px; height: 82px; font-size: 40px; }
  .tag-large-brut { left: 728px; top: 670px; width: 254px; height: 92px; font-size: 40px; }
  .tag-on-brut { left: 142px; top: 510px; width: 106px; height: 45px; font-size: 17px; }
  .tag-on-rose { left: 482px; top: 510px; width: 110px; height: 46px; font-size: 17px; }
</style>
</head>
<body>
<main class="canvas">

  <svg class="bottles" width="1200" height="960" viewBox="0 0 1200 960" role="img" aria-label="Two sparkling wine bottles: a green Brut bottle and a clear rosé bottle, each with a silver foil neck">
    <defs>
      <path id="bottle-outline" d="M158,10 L232,10 Q240,10 240,22 L240,250 Q242,330 305,395 Q323,415 323,450 L323,900 Q323,915 308,915 L82,915 Q68,915 68,900 L68,450 Q68,415 86,395 Q148,330 150,250 L150,22 Q150,10 158,10 Z"/>
      <clipPath id="bottle-clip"><use href="#bottle-outline"/></clipPath>
      <linearGradient id="green-glass" x1="0" x2="1">
        <stop offset="0" stop-color="var(--glass-green)"/>
        <stop offset="0.55" stop-color="var(--glass-green-light)"/>
        <stop offset="1" stop-color="var(--glass-green)"/>
      </linearGradient>
      <linearGradient id="rose-glass" x1="0" x2="1">
        <stop offset="0" stop-color="var(--glass-rose)"/>
        <stop offset="0.5" stop-color="var(--glass-rose-light)"/>
        <stop offset="1" stop-color="var(--glass-rose)"/>
      </linearGradient>
      <linearGradient id="foil" x1="0" x2="1">
        <stop offset="0" stop-color="var(--foil-dark)"/>
        <stop offset="0.45" stop-color="var(--foil-light)"/>
        <stop offset="1" stop-color="var(--foil-dark)"/>
      </linearGradient>
    </defs>
    <g class="bottle-brut">
      <use href="#bottle-outline" fill="url(#green-glass)"/>
      <rect x="0" y="0" width="400" height="370" fill="url(#foil)" clip-path="url(#bottle-clip)"/>
    </g>
    <g class="bottle-rose" transform="translate(342 0)">
      <use href="#bottle-outline" fill="url(#rose-glass)"/>
      <rect x="0" y="0" width="400" height="300" fill="url(#foil)" clip-path="url(#bottle-clip)"/>
    </g>
  </svg>

  <!-- Front label: on Brut bottle -->
  <section class="front-label label-on-brut">
    <svg class="label-shape" viewBox="0 0 360 220" preserveAspectRatio="none" aria-hidden="true">
      <path d="M20,60 Q40,55 45,30 Q110,30 150,18 Q180,2 210,18 Q250,30 315,30 Q320,55 340,60 Q358,110 340,160 Q320,165 315,190 Q250,190 210,202 Q180,218 150,202 Q110,190 45,190 Q40,165 20,160 Q2,110 20,60 Z" fill="var(--label-cream)" stroke="var(--ink-blue)" stroke-width="6"/>
    </svg>
    <div class="label-text">
      <p class="method">METHOD<br>TRADITIONELLE</p>
      <h2 class="brand-name">Jardin Lumineux</h2>
      <p class="appellation-title">CREMANT DE LIMOUX</p>
      <p class="appellation-full">APPELLATION CREMANT DE LIMOUX CONTROLEE</p>
      <p class="origin">PRODUCT OF FRANCE</p>
    </div>
  </section>

  <!-- Front label: on Rosé bottle -->
  <section class="front-label label-on-rose">
    <svg class="label-shape" viewBox="0 0 360 220" preserveAspectRatio="none" aria-hidden="true">
      <path d="M20,60 Q40,55 45,30 Q110,30 150,18 Q180,2 210,18 Q250,30 315,30 Q320,55 340,60 Q358,110 340,160 Q320,165 315,190 Q250,190 210,202 Q180,218 150,202 Q110,190 45,190 Q40,165 20,160 Q2,110 20,60 Z" fill="var(--label-cream)" stroke="var(--ink-blue)" stroke-width="6"/>
    </svg>
    <div class="label-text">
      <p class="method">METHOD<br>TRADITIONELLE</p>
      <h2 class="brand-name">Jardin Lumineux</h2>
      <p class="appellation-title">CREMANT DE LIMOUX</p>
      <p class="appellation-full">APPELLATION CREMANT DE LIMOUX CONTROLEE</p>
      <p class="origin">PRODUCT OF FRANCE</p>
    </div>
  </section>

  <!-- Front label: flat artwork -->
  <section class="front-label label-large">
    <svg class="label-shape" viewBox="0 0 360 220" preserveAspectRatio="none" aria-hidden="true">
      <path d="M20,60 Q40,55 45,30 Q110,30 150,18 Q180,2 210,18 Q250,30 315,30 Q320,55 340,60 Q358,110 340,160 Q320,165 315,190 Q250,190 210,202 Q180,218 150,202 Q110,190 45,190 Q40,165 20,160 Q2,110 20,60 Z" fill="var(--label-cream)" stroke="var(--ink-blue)" stroke-width="5"/>
    </svg>
    <div class="label-text">
      <p class="method">METHOD<br>TRADITIONELLE</p>
      <h1 class="brand-name">Jardin Lumineux</h1>
      <p class="appellation-title">CREMANT DE LIMOUX</p>
      <p class="appellation-full">APPELLATION CREMANT DE LIMOUX CONTROLEE</p>
      <p class="origin">PRODUCT OF FRANCE</p>
    </div>
  </section>

  <!-- Neck style tags -->
  <div class="style-tag tag-on-brut">
    <svg viewBox="0 0 200 90" preserveAspectRatio="none" aria-hidden="true"><ellipse cx="100" cy="45" rx="96" ry="41" fill="var(--label-cream)" stroke="var(--ink-blue)" stroke-width="6"/></svg>
    <span>BRUT</span>
  </div>
  <div class="style-tag tag-on-rose">
    <svg viewBox="0 0 200 90" preserveAspectRatio="none" aria-hidden="true"><ellipse cx="100" cy="45" rx="96" ry="41" fill="var(--label-cream)" stroke="var(--ink-blue)" stroke-width="6"/></svg>
    <span>ROSE</span>
  </div>
  <div class="style-tag tag-large-rose">
    <svg viewBox="0 0 200 90" preserveAspectRatio="none" aria-hidden="true"><ellipse cx="100" cy="45" rx="97" ry="42" fill="var(--label-cream)" stroke="var(--ink-blue)" stroke-width="4"/></svg>
    <span>ROSE</span>
  </div>
  <div class="style-tag tag-large-brut">
    <svg viewBox="0 0 200 90" preserveAspectRatio="none" aria-hidden="true"><ellipse cx="100" cy="45" rx="97" ry="42" fill="var(--label-cream)" stroke="var(--ink-blue)" stroke-width="4"/></svg>
    <span>BRUT</span>
  </div>

</main>
</body>
</html>
```